Quarry Vale Business Cards

We need to design some upbeat business cards. We are an Industrial Rope Access Company/Height Safety Company that specialize in Rope Access, Confined Space, Anchor Points, Safety Systems, PPE Inspecions and Rigging.
Company name is Quarry Vale Ltd
Card is for Reggie Stanton the Company Director
His mobile number is 027 816 4920 and email is reggie@quarryvale.co.nz. Website address is www.quarryvale.co.nz.
We will post some pictures below to ensure you get a good idea of what we do.

```html
<!DOCTYPE html>
<html lang="en">
<head>
<meta charset="utf-8">
<title>Quarry Vale Business Cards</title>
<link href="https://fonts.googleapis.com/css2?family=Exo+2:wght@400;500;700&display=swap" rel="stylesheet">
<style>
  :root {
    --brand-blue: #2d3f9a;
    --brand-blue-dark: #24347f;
    --card-cream: #efeadb;
    --ink-grey: #5a5a5a;
    --rule-grey: #8a8a8a;
    --stage: #e4e4e4;
    --white: #ffffff;
  }
  * { box-sizing: border-box; margin: 0; padding: 0; }
  html, body {
    width: 1200px; height: 786px; overflow: hidden;
    background: var(--stage);
    font-family: "Exo 2", sans-serif;
  }
  .canvas { position: relative; width: 1200px; height: 786px; }
  .card {
    position: absolute; top: 238px;
    width: 540px; height: 309px;
    box-shadow: 0 6px 18px rgba(0,0,0,0.18);
    overflow: hidden;
  }
  /* Front */
  .card--front { left: 40px; background: var(--card-cream); }
  .front__name-mark {
    position: absolute; left: 210px; top: 52px;
    font-weight: 700; font-size: 44px; letter-spacing: 0.5px;
    color: var(--brand-blue);
    white-space: nowrap;
  }
  .front__rule {
    position: absolute; left: 236px; top: 150px;
    width: 274px; height: 1px; background: var(--rule-grey);
  }
  .front__contacts {
    position: absolute; left: 28px; top: 158px;
    width: 200px;
    list-style: none; font-size: 12.5px; color: var(--ink-grey);
    line-height: 19px;
  }
  .front__contacts li { display: flex; align-items: center; gap: 7px; white-space: nowrap; }
  .front__contacts svg { width: 10px; height: 10px; fill: var(--brand-blue); flex: none; }
  .front__person {
    position: absolute; right: 30px; top: 186px; text-align: right;
  }
  .person__name { font-weight: 700; font-size: 17px; color: var(--brand-blue); white-space: nowrap; }
  .person__role { font-size: 12.5px; color: var(--ink-grey); }
  .front__band {
    position: absolute; left: 0; bottom: 0; width: 100%; height: 8px;
    display: flex;
  }
  .front__band-blue { flex: 1; background: var(--brand-blue); }
  .front__band-grey { width: 60px; background: var(--rule-grey); }
  /* Back */
  .card--back { left: 620px; background: var(--brand-blue); }
  .back__texture {
    position: absolute; inset: 0;
    background: linear-gradient(135deg, var(--brand-blue) 0%, var(--brand-blue-dark) 100%);
  }
  .back__name-mark {
    position: absolute; left: 0; right: 0; top: 126px; text-align: center;
    font-weight: 700; font-size: 50px; color: var(--white); letter-spacing: 0.5px;
    white-space: nowrap;
  }
</style>
</head>
<body>
<main class="canvas">
  <section class="card card--front" aria-label="Card front">
    <div class="front__name-mark">Quarry Vale</div>
    <div class="front__rule"></div>
    <ul class="front__contacts">
      <li><svg viewBox="0 0 10 10"><path d="M2 0.5 L4 2.5 L3 3.8 Q4.5 6 6.2 7 L7.5 6 L9.5 8 L8 9.5 Q3.5 9 0.5 2 Z"/></svg>027 816 4920</li>
      <li><svg viewBox="0 0 10 10"><path d="M0.5 2 H9.5 V8 H0.5 Z M1 2.5 L5 5.5 L9 2.5" fill="none" stroke="#2d3f9a" stroke-width="1"/></svg>reggie@quarryvale.co.nz</li>
      <li><svg viewBox="0 0 10 10"><circle cx="5" cy="5" r="4.5"/></svg>www.quarryvale.co.nz</li>
    </ul>
    <div class="front__person">
      <div class="person__name">Reggie Stanton</div>
      <div class="person__role">Director</div>
    </div>
    <div class="front__band"><span class="front__band-blue"></span><span class="front__band-grey"></span></div>
  </section>

  <section class="card card--back" aria-label="Card back">
    <div class="back__texture" role="img" aria-label="Faint repeating company-name texture across the blue background"></div>
    <div class="back__name-mark">Quarry Vale</div>
  </section>
</main>
</body>
</html>
```